Bref créative
business card and letter head
TCW Roofing & Decks, LLC
Corporate
Dale Harrington
Project Manager / Estimator
7426-B Ferncliff
Houston, TX 77094
daleh4182@quorvix.com
Logo for TCW Roofing & Decks, LLC

```html
<!DOCTYPE html>
<html lang="en">
<head>
<meta charset="utf-8">
<title>TCW Roofing &amp; Decks, LLC — Business Card</title>
<link rel="stylesheet" href="https://fonts.googleapis.com/css2?family=Tinos:wght@400;700&display=swap">
<style>
  :root {
    --backdrop: #e9e6e1;
    --card: #ffffff;
    --navy: #1f3a68;
    --ink: #2a2a2a;
    --shadow: rgba(0,0,0,0.18);
  }
  * { margin: 0; padding: 0; box-sizing: border-box; }
  html, body { width: 1200px; height: 871px; overflow: hidden; }
  body {
    background: var(--backdrop);
    font-family: "Tinos", "Times New Roman", serif;
    color: var(--ink);
    position: relative;
  }
  .card {
    position: absolute;
    left: 330px;
    width: 540px;
    height: 309px;
    background: var(--card);
    box-shadow: 0 6px 18px var(--shadow);
  }
  .card--front { top: 96px; }
  .card--back { top: 466px; }

  .brand {
    position: absolute;
    left: 0;
    right: 0;
    display: flex;
    justify-content: center;
    align-items: center;
    gap: 10px;
    color: var(--navy);
    font-size: 28px;
    font-weight: 400;
    line-height: 1;
    white-space: nowrap;
  }
  .brand__square {
    width: 14px;
    height: 14px;
    background: var(--navy);
    flex: none;
  }
  .card--front .brand { top: 140px; }
  .card--back .brand { top: 48px; }

  .contact {
    position: absolute;
    left: 70px;
    top: 136px;
    font-size: 17px;
    line-height: 21px;
    list-style: none;
  }
  .contact li { display: flex; align-items: center; }
  .contact svg { width: 13px; height: 13px; margin-right: 6px; fill: var(--ink); flex: none; }

  .person {
    position: absolute;
    right: 56px;
    bottom: 34px;
    text-align: right;
    font-size: 14px;
    line-height: 17px;
  }
  .person__name { font-weight: 700; }

  .corner-square {
    position: absolute;
    right: 0;
    bottom: 34px;
    width: 22px;
    height: 28px;
    background: var(--navy);
  }
</style>
</head>
<body>
  <section class="card card--front" aria-label="Business card front">
    <div class="brand">
      <span class="brand__square" aria-hidden="true"></span>
      <span class="brand__name">TCW Roofing &amp; Decks, LLC</span>
    </div>
  </section>

  <section class="card card--back" aria-label="Business card back">
    <div class="brand">
      <span class="brand__square" aria-hidden="true"></span>
      <span class="brand__name">TCW Roofing &amp; Decks, LLC</span>
    </div>

    <ul class="contact">
      <li>7426-B Ferncliff</li>
      <li>Houston, TX 77094</li>
      <li>
        <svg viewBox="0 0 16 16" aria-hidden="true"><path d="M3.5 1.5l2.5 0 1.2 3.2-1.6 1.2c.9 1.9 2.4 3.4 4.3 4.3l1.2-1.6 3.2 1.2v2.5c0 .9-.8 1.7-1.7 1.7C6.6 14 2 9.4 2 3.2c0-.9.6-1.7 1.5-1.7z"/></svg>
        713-555-0142
      </li>
      <li>
        <svg viewBox="0 0 16 16" aria-hidden="true"><rect x="1" y="6" width="14" height="8" rx="1"/><rect x="4" y="2" width="8" height="4"/></svg>
        713-555-0187
      </li>
      <li>
        <svg viewBox="0 0 16 16" aria-hidden="true"><rect x="4" y="1" width="8" height="14" rx="1.5"/></svg>
        832-555-0163
      </li>
      <li>
        <svg viewBox="0 0 16 16" aria-hidden="true"><path d="M1 3h14v10H1z M1 3l7 6 7-6" stroke="#fff" stroke-width="1"/></svg>
        daleh4182@quorvix.com
      </li>
    </ul>

    <div class="person">
      <div class="person__name">Dale Harrington</div>
      <div class="person__title">Project Manager / Estimator</div>
    </div>

    <div class="corner-square"></div>
  </section>
</body>
</html>
```